pet resort day care for our buisiness

we need a new web design for our pet center in Florida , we are provide the following services -
1. dog day car
2.dog/cat boarding
3. dog grooming
4. Dog training
5.pet food toy and clothing
our current websit is -http://www.wellowbyanimalhaven.com/
we are looking for a fresh new design that will reflect the change that we have made in the vusness from renovationnto the facelaty new management and new servises
Target Market(s)
Dog Lover , Upmarket
Industry/Entity Type
Pet
Number of Pages Required
5+ page
Font styles to use
Sans Serif
Requirements
Must have
- clean design , easy to understand and navigate , our target is the upmarket costumer how are dog lover
Should not have
- NOOO of the shelf design , confusing design , brown colors

```html
<!DOCTYPE html>
<html lang="en">
<head>
<meta charset="utf-8">
<title>Wellowby Pet Center</title>
<link href="https://fonts.googleapis.com/css2?family=Damion&family=Arimo:wght@400;700&family=Varela+Round&display=swap" rel="stylesheet">
<style>
:root{
  --pink:#ee3f66;
  --lime:#c6dc5c;
  --slate:#56606c;
  --ink:#333a42;
  --white:#ffffff;
}
*{box-sizing:border-box;margin:0;padding:0}
html,body{width:693px;height:1200px;overflow:hidden;background:var(--white)}
body{position:relative;font-family:"Varela Round",sans-serif;color:var(--ink)}
.abs{position:absolute}

/* header */
.site-header{left:0;top:0;width:693px;height:39px;background:var(--white)}
.brand{left:48px;top:4px;display:flex;align-items:center;gap:4px}
.brand-dot{width:10px;height:10px;border-radius:50%;background:var(--lime)}
.brand-name{font-family:"Varela Round",sans-serif;font-size:10px;color:var(--pink)}
.main-nav{left:166px;top:14px;display:flex;gap:9px;font-family:"Arimo",sans-serif;font-size:7.4px;color:var(--slate);text-transform:uppercase}
.main-nav .active{color:var(--pink);position:relative}
.main-nav .active::before,.main-nav .active::after{content:"";position:absolute;left:50%;margin-left:-2px;border-left:2px solid transparent;border-right:2px solid transparent}
.main-nav .active::before{top:-6px;border-top:3px solid var(--pink)}
.main-nav .active::after{bottom:-7px;border-bottom:3px solid var(--pink)}
.phone{left:580px;top:13px;display:flex;align-items:center;gap:6px;font-size:8px;color:var(--pink)}

/* hero */
.hero{left:0;top:39px;width:693px;height:347px;background:radial-gradient(ellipse at 45% 45%,#e7d3bd 0%,#c98a4f 30%,#a3642f 48%,#d9d6d2 70%,#9aa0a6 100%)}
.hero-title{left:0;top:171px;width:693px;text-align:center;font-family:"Arimo",sans-serif;font-weight:700;font-size:22px;letter-spacing:-.5px;color:var(--pink);text-transform:uppercase}
.hero-sub{left:230px;top:202px;width:230px;text-align:center;font-family:"Arimo",sans-serif;font-size:6px;line-height:9px;color:#222;text-transform:uppercase}
.social{left:654px;top:136px;width:39px}
.social span{display:flex;align-items:center;justify-content:center;height:39px}
.social span i{width:12px;height:12px;border-radius:50%;background:var(--white);display:block}
.social .s1{background:var(--lime)}
.social .s2,.social .s3,.social .s4{background:var(--slate)}

/* welcome */
.welcome-title{left:0;top:392px;width:693px;text-align:center;font-family:"Damion",cursive;font-size:20px;color:var(--pink)}
.welcome-text{left:150px;top:426px;width:393px;text-align:center;font-size:8.4px;line-height:11.5px;color:var(--ink)}
.map-btn{left:328px;top:458px;width:54px;height:14px;border-radius:2px;background:var(--slate);color:var(--lime);font-size:8px;line-height:14px;text-align:center}

.feature{top:497px;width:160px;text-align:center}
.feature .circle{width:68px;height:68px;border-radius:50%;margin:0 auto;display:flex;align-items:center;justify-content:center}
.feature h3{font-family:"Damion",cursive;font-weight:400;font-size:14px;color:var(--pink);margin-top:11px}
.feature p{font-size:8px;color:var(--ink);margin-top:1px}
.f1{left:110px}.f1 .circle{background:var(--lime)}
.f2{left:267px}.f2 .circle{background:var(--pink)}
.f3{left:423px}.f3 .circle{background:var(--pink)}

/* services */
.services{left:0;top:620px;width:693px;height:345px;background:linear-gradient(100deg,#3f3b33 0%,#7d6a3e 30%,#b4914c 55%,#d9c9ab 75%,#a88a55 100%)}
.service-row{left:0;width:693px;height:69px;border-bottom:1px solid var(--lime);display:flex;align-items:center}
.service-row:last-child{border-bottom:none}
.service-row.open{background:rgba(60,66,74,.85)}
.service-row h2{width:110px;margin-left:38px;font-family:"Arimo",sans-serif;font-weight:700;font-size:14.5px;letter-spacing:-.4px;color:var(--lime)}
.service-row .arrow{width:0;height:0;border-left:7px solid var(--lime);border-top:3.5px solid transparent;border-bottom:3.5px solid transparent;margin-left:0}
.service-row .desc{margin-left:20px;margin-top:-10px;font-size:6.6px;line-height:13px;color:var(--lime)}

/* booking */
.book-title{left:0;top:973px;width:693px;text-align:center;font-family:"Damion",cursive;font-size:20px;color:var(--pink)}
.field{left:246px;width:201px;height:24px;border:1px solid var(--slate);border-radius:6px;padding-left:12px;font-size:8px;line-height:22px;color:var(--pink)}
.submit{left:393px;top:1135px;width:54px;height:15px;border-radius:4px;background:var(--slate);color:var(--lime);font-size:8px;line-height:15px;text-align:center}

/* footer */
.site-footer{left:0;top:1173px;width:693px;height:27px;background:var(--slate);font-family:"Arimo",sans-serif;font-size:5px;color:var(--lime);text-transform:uppercase;display:flex;justify-content:center;align-items:center;gap:26px}
.site-footer em{font-style:italic}
</style>
</head>
<body>

<header class="site-header abs">
  <div class="brand abs"><span class="brand-dot"></span><span class="brand-name">Wellowby</span></div>
  <nav class="main-nav abs">
    <span class="active">Home</span><span>Boarding</span><span>Daycare</span><span>Grooming</span><span>Training</span><span>Boutique</span><span>Blog</span><span>Contact</span><span>About Us</span>
  </nav>
  <div class="phone abs">
    <svg width="9" height="9" viewBox="0 0 10 10"><circle cx="5" cy="5" r="5" fill="#ee3f66"/><path d="M3.2 2.6c.4 1.8 1.8 3.4 3.8 4.4l.6-.9-1-.6-.5.5c-.8-.5-1.4-1.2-1.8-2l.5-.4-.5-1.1z" fill="#fff"/></svg>
    <span>954-555-0142</span>
  </div>
</header>

<section class="hero abs" role="img" aria-label="Photo of a beagle looking up, close-up portrait"></section>
<h1 class="hero-title abs">Love to play &amp; meet my buddies.</h1>
<p class="hero-sub abs">Neque porro quisquam est qui dolorem ipsum quia dolor sit amet, consectetur, adipisci velit.</p>

<aside class="social abs">
  <span class="s1"><i></i></span><span class="s2"><i></i></span><span class="s3"><i></i></span><span class="s4"><i></i></span>
</aside>

<h2 class="welcome-title abs">Welcome to Wellowby Pet Center!</h2>
<p class="welcome-text abs">A pet paradise providing the best pet care in the greater Fort Lauderdale FL area. Professional cat &amp; dog boarding, doggy daycare, pet grooming, training, holistic foods &amp; pet boutique.</p>
<div class="map-btn abs">View Map ▾</div>

<div class="feature f1 abs">
  <div class="circle">
    <svg width="32" height="30" viewBox="0 0 32 30" fill="none" stroke="#ee3f66" stroke-width="2.4"><rect x="3" y="5" width="22" height="22" rx="2"/><line x1="3" y1="11" x2="25" y2="11"/><line x1="9" y1="2" x2="9" y2="7"/><line x1="19" y1="2" x2="19" y2="7"/><path d="M13 22l12-12 3 3-12 12-4 1z" fill="#ee3f66"/></svg>
  </div>
  <h3>Reservation</h3>
  <p>What Time Is Best For You?</p>
</div>
<div class="feature f2 abs">
  <div class="circle">
    <svg width="20" height="34" viewBox="0 0 20 34"><text x="10" y="28" text-anchor="middle" font-family="Arimo,sans-serif" font-weight="700" font-size="30" fill="#fff">$</text></svg>
  </div>
  <h3>Our Rates</h3>
  <p>Boarding, Daycare, Grooming</p>
</div>
<div class="feature f3 abs">
  <div class="circle">
    <svg width="34" height="30" viewBox="0 0 34 30" fill="none" stroke="#fff" stroke-width="2.2"><path d="M3 3h28l2 8H1z"/><path d="M4 11v17h26V11"/><rect x="10" y="16" width="14" height="8"/></svg>
  </div>
  <h3>Boutique &amp; Holistic</h3>
  <p>High Quality Pet Products.</p>
</div>

<section class="services abs" role="img" aria-label="Photo of a fluffy cream puppy sitting in a field with yellow flowers">
  <div class="service-row open abs" style="top:0">
    <h2>BOARDING</h2><span class="arrow"></span>
    <p class="desc">Wellowby Pet Center in Fort Lauderdale FL is a unique pet resort with luxurious boarding accommodations.<br>Taking cat &amp; dog boarding to a new standard of excellence.</p>
  </div>
  <div class="service-row abs" style="top:69px"><h2>DAYCARE</h2><span class="arrow"></span></div>
  <div class="service-row abs" style="top:138px"><h2>GROOMING</h2><span class="arrow"></span></div>
  <div class="service-row abs" style="top:207px"><h2>TRAINING</h2><span class="arrow"></span></div>
  <div class="service-row abs" style="top:276px"><h2>BOUTIQUE</h2></div>
</section>

<h2 class="book-title abs">Book An Appointment Today</h2>
<div class="field abs" style="top:1014px">Your Name</div>
<div class="field abs" style="top:1046px">Email Address</div>
<div class="field abs" style="top:1079px">Phone Number</div>
<div class="field abs" style="top:1111px">Message</div>
<div class="submit abs">Submit</div>

<footer class="site-footer abs">
  <span>© 2013 Wellowby Pet Center. All rights reserved.</span>
  <em>Privacy Policy</em>
</footer>

</body>
</html>
```